Real Estate Flyer (Brenton Property)

We need a color CMYK high resolution, print quality horizontal real estate property flyer designed in the sizes of 10" wide and 6.7425" tall and another one in 11" wide and 8.5" tall.
Ad should be professionally looking to U.S. standards. It should be sleek, modern yet classy.
We uploaded in Briefs logo files, agent photo, 2 photos of the property (Must use both) and a sample of a flyer for Vayle Morrow Luxury Residence. We like how the overlay atop the first photo in the Vayle Morrow flyer with the company logo in the overlay. We'd like to incorporate that with our logo, the background color of the overlay should match that of our logo. DON'T CHANGE LOGO COLORS. Only use two colors in ad (exact logo blue color and white). The text in the overlay must be "FOR SALE - Potential Income Producing Commercial Office Building". Other details that should be prominent underneath are "42 Brenton Dr., Schaumburg, IL 60174 - Asking Price: $650,000".
Add "Residential & Commercial" under our company logo in italic font.
Add in flyer: "Located seconds away from the Kettering Rd. & Palden Rd. Intersection"
Add in flyer:
- Completely vacant
- 10,000 sq. ft. building
- 55 Car Parking
- 1.38 acre lot
- Over 20 offices and 5 bathrooms.
- Lease out individual office spaces for great monthly cash flow
Put agent's photo and following details professionally displayed:
Dev Marlo
Managing Broker
847-555-0148
dev.marlo@qtnhomes-example.com
Add from Briefs fair housing logo and PLX logo near agent's information. Logos should be small but yet visible to understand text.
Add at bottom of the ad with separation near agent details:
Looking to Buy or Sell?
I’m your one-stop, full service licensed real estate broker.
I deal with all types of real estate properties: Homes, Condos, Townhomes, Multi-Unit Apartment Buildings and Commercial Spaces.
Let My Experience Guide You Through Every Step of the Process!
Fine print:
©2018 QTN Homes, Inc. All Rights Reserved.

```html
<!DOCTYPE html>
<html lang="en">
<head>
<meta charset="utf-8">
<title>Brenton Property – For Sale Flyer</title>
<link href="https://fonts.googleapis.com/css2?family=Arimo:wght@400;700&family=PT+Sans:ital,wght@0,400;0,700;1,400&display=swap" rel="stylesheet">
<style>
  :root {
    --brand-blue: #1e4486;
    --brand-blue-deep: #173a76;
    --white: #ffffff;
    --ink: #1e2a44;
  }
  * { box-sizing: border-box; margin: 0; padding: 0; }
  html, body { width: 1200px; height: 798px; overflow: hidden; background: #e9ebef; }
  .flyer {
    position: relative;
    width: 1200px; height: 798px;
    background: var(--white);
    border: 18px solid var(--brand-blue);
    font-family: "PT Sans", Arial, sans-serif;
    color: var(--ink);
  }
  .hero-photo {
    position: absolute; left: 0; top: 0; width: 1164px; height: 276px;
    background: linear-gradient(180deg, #c9a98a 0%, #e6c9a3 35%, #b9a48e 62%, #5c5148 100%);
  }
  .overlay-band {
    position: absolute; left: 0; top: 276px; width: 1164px; height: 124px;
    background: linear-gradient(180deg, rgba(30,68,134,0.93), var(--brand-blue));
    color: var(--white);
  }
  .overlay-title {
    position: absolute; left: 63px; top: 6px;
    font-family: "Arimo", Arial, sans-serif; font-weight: 700;
    font-size: 30px; line-height: 33px;
  }
  .overlay-address {
    position: absolute; left: 63px; top: 84px;
    font-size: 22px; line-height: 24px;
  }
  .overlay-divider {
    position: absolute; left: 819px; top: 15px; width: 2px; height: 92px;
    background: var(--white);
  }
  .brand {
    position: absolute; left: 870px; top: 24px; width: 220px; text-align: center;
  }
  .brand-name {
    display: flex; align-items: center; justify-content: center; gap: 10px;
    font-family: "PT Sans", Arial, sans-serif; font-weight: 700;
    font-size: 34px; line-height: 40px; letter-spacing: 1px;
  }
  .brand-square { width: 16px; height: 16px; background: var(--white); }
  .brand-tagline {
    margin-top: 20px; font-style: italic; font-size: 10px; letter-spacing: 0.3px;
  }
  .location-line {
    position: absolute; left: 30px; top: 412px; width: 1104px; text-align: center;
    font-family: "Arimo", Arial, sans-serif; font-weight: 700;
    font-size: 19px; color: var(--brand-blue); letter-spacing: 0.3px;
  }
  .features {
    position: absolute; top: 483px; list-style: none;
    font-size: 11px; line-height: 17px;
  }
  .features li { position: relative; padding-left: 14px; }
  .features li::before {
    content: ""; position: absolute; left: 0; top: 6px;
    width: 5px; height: 5px; border-radius: 50%; background: var(--brand-blue-deep);
  }
  .features-left { left: 65px; }
  .features-right { left: 285px; width: 190px; }
  .side-photo {
    position: absolute; left: 552px; top: 448px; width: 568px; height: 151px;
    border: 2px solid var(--brand-blue);
    background: linear-gradient(180deg, #d8c8b8 0%, #e3cba8 45%, #a99a88 75%, #4e4a47 100%);
  }
  .agent-photo {
    position: absolute; left: 59px; top: 564px; width: 151px; height: 162px;
    border: 2px solid var(--brand-blue);
    background: linear-gradient(180deg, #eef0f3 0%, #d9dde3 55%, #2f3238 100%);
  }
  .agent {
    position: absolute; left: 230px; top: 592px;
  }
  .agent-name {
    font-family: "Arimo", Arial, sans-serif; font-weight: 700;
    font-size: 22px; color: var(--brand-blue);
  }
  .agent-role { font-size: 19px; margin-top: 4px; }
  .agent-contact { margin-top: 18px; font-size: 18px; line-height: 26px; }
  .agent-contact li { list-style: none; display: flex; align-items: center; gap: 8px; }
  .agent-contact svg { width: 18px; height: 18px; }
  .pitch { position: absolute; left: 552px; top: 614px; width: 580px; }
  .pitch-title {
    font-family: "Arimo", Arial, sans-serif; font-weight: 700;
    font-size: 20px; color: var(--brand-blue);
  }
  .pitch-list { list-style: none; margin-top: 12px; font-size: 11px; line-height: 17px; }
  .pitch-list li { position: relative; padding-left: 26px; }
  .pitch-list li::before {
    content: ""; position: absolute; left: 2px; top: 6px;
    width: 5px; height: 5px; border-radius: 50%; background: var(--brand-blue-deep);
  }
  .badges { position: absolute; left: 975px; top: 702px; display: flex; gap: 12px; align-items: center; }
  .badge-housing { width: 44px; height: 40px; background: #222; }
  .badge-listing { width: 88px; height: 34px; border: 2px solid #222; }
</style>
</head>
<body>
  <main class="flyer">
    <div class="hero-photo" role="img" aria-label="Photo of the two-storey white commercial office building with dormers at sunset, cars parked in front"></div>

    <section class="overlay-band">
      <h1 class="overlay-title">FOR SALE - Potential Income Producing<br>Commercial Office Building</h1>
      <p class="overlay-address">42 Brenton Dr., Schaumburg, IL 60174 - Asking Price: $650,000</p>
      <div class="overlay-divider"></div>
      <div class="brand">
        <div class="brand-name"><span class="brand-square"></span>QTN HOMES</div>
        <p class="brand-tagline">RESIDENTIAL &amp; COMMERCIAL</p>
      </div>
    </section>

    <h2 class="location-line">"LOCATED SECONDS AWAY FROM THE KETTERING RD. &amp; PALDEN RD. INTERSECTION"</h2>

    <ul class="features features-left">
      <li>Completely vacant</li>
      <li>10,000 sq. ft. building</li>
      <li>55 Car Parking</li>
    </ul>
    <ul class="features features-right">
      <li>1.38 acre lot</li>
      <li>Over 20 offices and 5 bathrooms.</li>
      <li>Lease out individual office spaces for great monthly cash flow</li>
    </ul>

    <div class="side-photo" role="img" aria-label="Second photo of the office building seen along its side, with trees and parking lot at dusk"></div>

    <div class="agent-photo" role="img" aria-label="Portrait photo of the agent in a dark suit"></div>
    <div class="agent">
      <h3 class="agent-name">DEV MARLO</h3>
      <p class="agent-role">Managing Broker</p>
      <ul class="agent-contact">
        <li>
          <svg viewBox="0 0 24 24" fill="none" stroke="#1e4486" stroke-width="1.8"><path d="M5 3h4l2 5-2.5 1.5a11 11 0 0 0 6 6L16 13l5 2v4a2 2 0 0 1-2 2A17 17 0 0 1 3 5a2 2 0 0 1 2-2z"/></svg>
          847-555-0148
        </li>
        <li>
          <svg viewBox="0 0 24 24" fill="none" stroke="#1e4486" stroke-width="1.8"><rect x="3" y="5" width="18" height="14"/><path d="M3 5l9 8 9-8"/></svg>
          dev.marlo@qtnhomes-example.com
        </li>
      </ul>
    </div>

    <section class="pitch">
      <h3 class="pitch-title">LOOKING TO BUY OR SELL?</h3>
      <ul class="pitch-list">
        <li>I’m your one-stop, full service licensed real estate broker.</li>
        <li>I deal with all types of real estate properties: Homes, Condos, Townhomes, Multi-Unit Apartment Buildings and Commercial Spaces.</li>
        <li>Let My Experience Guide You Through Every Step of the Process!</li>
      </ul>
    </section>

    <div class="badges">
      <div class="badge-housing" role="img" aria-label="Fair housing badge"></div>
      <div class="badge-listing" role="img" aria-label="PLX listing badge"></div>
    </div>
  </main>
</body>
</html>
```